Flyer for The Quiet Meadow Renewal Ring

I am launching my new offering in my business at an event next Sunday where I have a booth and need a flyer advertising the offering, so the flyer needs to stand out for other practitioners that will also be there on the day offering there services.
This flyer is also what I will use for marketing on social media as well as on the day of the event. See the link below to the offering
http://carolinebirchwood.com.au/quiet-meadow-renewal-ring/

Target Market(s)

Women with body image issues - age range 25 - 65
Women with issues around food such as binge eating, emotional eating, eating disorders.

Industry/Entity Type

Health And Wellness

Font styles to use
Serif
Sans Serif
Script

Colors
f9d9e8
85cae6
cee9f5
fee18a
ffffff
eea4c8

Requirements
Must have
• Colours matching my overall website at carolinebirchwood.com.au - pinks, light blue, gold, white
• Imagery similiar to my Instagram, see below https://www.instagram.com/lanternfieldcarexq/
• - soft, warm, welcoming, nurturing, safe, inviting - see image on sales page for inspiration
• contact details
Should not have
• harsh dark colours or harsh lines

```html
<!DOCTYPE html>
<html lang="en">
<head>
<meta charset="utf-8">
<title>The Quiet Meadow Renewal Ring – Flyer</title>
<link href="https://fonts.googleapis.com/css2?family=Arapey&family=Dancing+Script:wght@600&family=Open+Sans:wght@400;600;700&display=swap" rel="stylesheet">
<style>
:root{
  --paper:#efeeef;
  --teal:#2ba3c2;
  --pink:#e1437d;
  --plum:#8c6aa8;
  --sky:#85cae6;
  --blush:#f9d9e8;
  --rose:#eea4c8;
  --ink:#3a3a3a;
  --white:#ffffff;
  --rule:#d2cfd3;
}
*{margin:0;padding:0;box-sizing:border-box}
html,body{width:998px;height:1200px;overflow:hidden;background:var(--paper)}
.flyer{position:relative;width:998px;height:1200px;background:var(--paper);font-family:"Open Sans",sans-serif;color:var(--ink);overflow:hidden}
.soft-wash{position:absolute;left:0;top:200px;width:620px;height:260px;background:radial-gradient(ellipse at 30% 60%,var(--blush),rgba(249,217,232,0) 70%)}
.hero-photo{position:absolute;left:0;top:0;width:520px;height:400px;border-radius:0 0 48px 0;background:linear-gradient(135deg,#9fb26a 0%,#c9c585 45%,#f3e2bf 100%)}
.brand{position:absolute;right:90px;top:48px;width:330px;text-align:center}
.brand-name{font-weight:600;font-size:30px;color:var(--pink);letter-spacing:.5px}
.offer-title{position:absolute;right:60px;top:118px;width:360px;text-align:center;font-family:"Dancing Script",cursive;font-weight:600;font-size:50px;line-height:1.15;background:linear-gradient(90deg,var(--pink),var(--plum) 60%,var(--teal));-webkit-background-clip:text;background-clip:text;color:transparent}
.serif{font-family:"Arapey",serif;font-weight:400}
.headline{position:absolute;left:0;width:998px;text-align:center}
.headline.one{top:440px;font-size:44px;color:var(--teal)}
.headline.two{top:492px;font-size:42px;color:var(--pink)}
.ticks{list-style:none;font-size:12.5px;line-height:1.45}
.ticks li{position:relative;padding-left:24px;margin-bottom:5px}
.ticks li::before{content:"";position:absolute;left:0;top:3px;width:12px;height:12px;border:1.6px solid var(--ink);border-radius:50%}
.ticks li::after{content:"";position:absolute;left:4px;top:5px;width:3px;height:6px;border:solid var(--ink);border-width:0 1.6px 1.6px 0;transform:rotate(45deg)}
.lead-left{position:absolute;left:90px;top:572px;width:410px}
.lead-right{position:absolute;left:525px;top:566px;width:395px}
.pill{display:inline-block;margin-top:6px;padding:6px 14px;font-weight:700;font-size:17px;color:var(--white);background:linear-gradient(90deg,var(--pink),var(--plum) 65%,var(--sky))}
.question{position:absolute;left:92px;top:732px;font-size:27px;color:var(--pink)}
.body-copy{position:absolute;left:92px;width:820px;font-size:15px;line-height:1.5}
.body-copy.a{top:772px}
.body-copy.b{top:826px}
.quote{color:var(--pink);font-weight:700}
.receive{position:absolute;left:92px;top:904px;font-size:29px;color:var(--teal)}
.benefits{position:absolute;left:92px;top:956px;width:410px;font-size:12px}
.benefits li{margin-bottom:3px}
.divider{position:absolute;left:520px;top:956px;width:1px;height:140px;background:var(--rule)}
.pricing{position:absolute;left:545px;top:952px;width:380px;font-size:13px;line-height:1.55}
.price{color:var(--pink);font-weight:700;font-size:15px}
.ready{position:absolute;left:545px;top:1036px;font-size:54px;line-height:1.1;background:linear-gradient(90deg,var(--pink),var(--plum) 55%,var(--teal));-webkit-background-clip:text;background-clip:text;color:transparent}
.footer-band{position:absolute;left:0;top:1118px;width:998px;height:52px;line-height:52px;text-align:center;color:var(--white);font-weight:600;letter-spacing:5px;font-size:14px;background:linear-gradient(90deg,var(--pink),var(--plum) 50%,var(--sky))}
</style>
</head>
<body>
<main class="flyer">
  <div class="soft-wash"></div>
  <div class="hero-photo" role="img" aria-label="Photo: woman meditating cross-legged outdoors in warm sunlight with green hills behind"></div>

  <div class="brand">
    <div class="brand-name">Caroline Birchwood</div>
  </div>
  <h1 class="offer-title">The Quiet Meadow Renewal Ring</h1>

  <h2 class="headline one serif">It’s time to make a commitment</h2>
  <h2 class="headline two serif">It’s time for YOU, to SHOW UP for YOU</h2>

  <ul class="ticks lead-left">
    <li>It’s time to truly let go……and finally heal, and find the peace that you so long for…</li>
    <li>You deserve to feel the freedom that comes with truly loving and accepting your body.</li>
    <li>You deserve the freedom that comes with experiencing a deeper trusting connection with your body, where you feel safe, at home.</li>
  </ul>
  <div class="lead-right">
    <ul class="ticks">
      <li>Can you even imagine a whole day that you didn’t hate your body, you didn’t fight with food, and you felt peaceful and at home with your body?</li>
      <li>Can you love the part of you, that hates your body?</li>
    </ul>
    <span class="pill">You can’t heal something you hate.</span>
  </div>

  <h3 class="question serif">Are you truly ready to make the commitment?</h3>
  <p class="body-copy a">How would it feel to be able to say, <span class="quote">“</span>I am free to love and accept my body<span class="quote">”</span>, and <span class="quote">“</span>I am free, connected and at peace to my body<span class="quote">”</span>?</p>
  <p class="body-copy b">I am inviting 10 women only into this six-week healing experience, as I personally know, that when we share our stories, it opens our hearts for other people to share their stories. It gives us the sense we are not alone in our journey’s.</p>

  <h3 class="receive serif">The women that come on this six-week journey will receive;</h3>
  <ul class="ticks benefits">
    <li>One 90mins one on one coaching session with me (which for the women that have attended the Friday circle previously, can be done before this healing circle begins);</li>
    <li>Private online group to continue support outside of the circle</li>
    <li>Homework outside of circle to support your healing</li>
    <li>Journal and other small gifts weekly</li>
  </ul>
  <div class="divider"></div>
  <p class="pricing">The financial investment in YOU, is <span class="price">$XX</span> for the six weeks. For the women that have attended the Friday night, Willow Song Sister Circle, you will receive a discount of $100, taking the price to <span class="price">$XX.</span></p>
  <p class="ready serif">Are you ready?</p>

  <div class="footer-band">www.carolinebirchwood.com.au</div>
</main>
</body>
</html>
```